Design for a Service-Based Estimate

We want a design for an Estimate that will always be sent in PDF format. The estimate or proposal is a critical document that needs to plainly show the service items, item description but also needs to be attractive and professional looking. Our current estimate deliverable is attached but it looks really basic like a Word document

```html
<!DOCTYPE html>
<html lang="en">
<head>
<meta charset="utf-8">
<title>Firmline Paving – Estimate</title>
<link rel="stylesheet" href="https://fonts.googleapis.com/css2?family=Source+Sans+3:wght@400;600;700;800&display=swap">
<style>
  :root{
    --backdrop:#e6ecec;
    --paper:#ffffff;
    --ink:#1f2326;
    --navy:#1d2a55;
    --rule-accent:#4ef3f7;
    --rule-grey:#4a4f52;
    --hairline:#dfe7e6;
    --footer-dark:#2b3236;
    --icon-cyan:#4ef3f7;
    --band-1:#4ffcfc;
    --band-2:#4cdcfd;
    --band-3:#35a9fb;
    --band-4:#2382fb;
    --band-5:#1562fb;
  }
  *{box-sizing:border-box;margin:0;padding:0}
  html,body{width:1200px;height:600px;overflow:hidden;background:var(--backdrop)}
  body{position:relative;font-family:"Source Sans 3",Arial,sans-serif;color:var(--ink)}

  .page{position:absolute;top:34px;width:377px;height:533px;background:var(--paper);box-shadow:0 2px 6px rgba(0,0,0,.12)}
  .page--estimate{left:108px}
  .page--terms{left:706px}

  .brand{position:absolute;left:43px;top:47px;font-weight:800;font-size:19px;letter-spacing:.6px;color:var(--navy);line-height:24px}
  .brand-mark{display:inline-block;width:9px;height:9px;background:var(--navy);margin-right:5px;vertical-align:2px}

  .header-rule{position:absolute;left:48px;top:89px;width:285px;height:2px}
  .header-rule .accent{position:absolute;left:0;top:0;width:93px;height:2px;background:var(--rule-accent)}
  .header-rule .base{position:absolute;left:93px;top:1px;right:0;height:.6px;background:var(--rule-grey)}

  .recipient{position:absolute;right:31px;top:144px;text-align:right;font-size:6.6px;line-height:9.4px;font-style:normal}
  .divider{position:absolute;left:48px;width:298px;height:.6px;background:var(--hairline)}

  .project{position:absolute;left:48px;width:298px;top:191px;text-align:center;font-size:6.6px}
  .project-title{font-weight:600;line-height:10px}
  .project-address{line-height:10px;margin-top:1px}
  .project-bid{margin-top:4px;line-height:10px}

  .items{position:absolute;left:48px;top:234px;width:298px;border-collapse:collapse;font-size:6.4px;line-height:8.4px}
  .items th{font-weight:700;vertical-align:bottom;padding:0 3px 3px;height:25px;border-top:.6px solid var(--hairline);border-bottom:.6px solid var(--hairline)}
  .items td{vertical-align:top;padding:4px 3px 3px;border-bottom:.6px solid var(--hairline)}
  .items .col-item{width:190px;text-align:left}
  .items .col-qty{width:35px;text-align:right}
  .items .col-um{width:20px;text-align:center}
  .items .col-unit{width:24px;text-align:right}
  .items .col-total{width:29px;text-align:right;font-weight:700;white-space:nowrap}
  .items .row-total td{height:21px;padding-top:5px}
  .items .label-total{font-weight:700;text-align:right}

  .footer{position:absolute;left:0;bottom:0;width:100%;height:50px}
  .footer-bar{position:absolute;left:0;top:0;width:100%;height:27px;background:var(--footer-dark);color:#fff;font-size:6.6px}
  .contact{position:absolute;top:9px;display:flex;align-items:center;gap:4px;line-height:9px}
  .contact--phone{left:25px}
  .contact--email{right:19px}
  .contact svg{width:10px;height:9px}
  .color-band{position:absolute;left:0;bottom:0;width:100%;height:23px;display:flex}
  .color-band span{flex:1}
  .color-band span:nth-child(1){background:var(--band-1)}
  .color-band span:nth-child(2){background:var(--band-2)}
  .color-band span:nth-child(3){background:var(--band-3)}
  .color-band span:nth-child(4){background:var(--band-4)}
  .color-band span:nth-child(5){background:var(--band-5)}

  .terms{position:absolute;left:41px;top:134px;width:299px;padding-bottom:10px;border:.6px solid var(--hairline);box-shadow:0 0 2px rgba(0,0,0,.05)}
  .terms-title{height:19px;border-bottom:.6px solid var(--hairline);text-align:center;font-size:7.6px;font-weight:400;line-height:19px;padding-top:1px}
  .terms-list{list-style:none;padding:8px 6px 0 18px;font-size:5.7px;line-height:8.4px}
  .terms-list li{position:relative}
  .terms-list li::before{content:"";position:absolute;left:-6.5px;top:3.3px;width:2px;height:2px;border-radius:50%;background:var(--ink)}

  .sign-line{position:absolute;left:48px;height:.6px;background:var(--ink)}
  .sign-label{position:absolute;left:48px;font-size:6.6px;line-height:9px}
</style>
</head>
<body>

<section class="page page--estimate">
  <div class="brand"><span class="brand-mark"></span>FIRMLINE PAVING</div>
  <div class="header-rule"><span class="accent"></span><span class="base"></span></div>

  <address class="recipient">
    To:<br>
    Dana Whitlow<br>
    418 Harbor Lane NE Fairview 30219<br>
    dwhitlow@mailbox.com
  </address>

  <div class="divider" style="top:185px"></div>

  <div class="project">
    <p class="project-title">Dana Whitlow New Concrete Pad</p>
    <p class="project-address">418 Harbor Lane NE Fairview 30219</p>
    <p class="project-bid">Bid#: 20-0182</p>
  </div>

  <table class="items">
    <thead>
      <tr>
        <th class="col-item">Item</th>
        <th class="col-qty">Quantity</th>
        <th class="col-um">U/M</th>
        <th class="col-unit">Unit<br>$</th>
        <th class="col-total">Total $</th>
      </tr>
    </thead>
    <tbody>
      <tr>
        <td class="col-item">Form, Pour &amp; Finish New Concrete Slab (24' x 24' x 4"). Includes: 3000psi Concrete Mix, Footer (12" x 8") with One (#5) Continuous Rebar, Wire Mesh Reinforcement and Saw-Cut Expansion Joints</td>
        <td class="col-qty">576</td>
        <td class="col-um">SF</td>
        <td class="col-unit">$8.65</td>
        <td class="col-total">$4,982.40</td>
      </tr>
      <tr>
        <td class="col-item">OPTIONAL: Add (2' x 24' x 4") Small Ramp Area</td>
        <td class="col-qty">48</td>
        <td class="col-um">SF</td>
        <td class="col-unit">$8.65</td>
        <td class="col-total">$415.20</td>
      </tr>
      <tr class="row-total">
        <td></td>
        <td></td>
        <td colspan="2" class="label-total">Total Price</td>
        <td class="col-total">$5,397.60</td>
      </tr>
    </tbody>
  </table>

  <footer class="footer">
    <div class="footer-bar">
      <div class="contact contact--phone">
        <svg viewBox="0 0 20 18" aria-hidden="true"><path d="M2 6c0-3 16-3 16 0v2h-4V6H6v2H2z M5 9h10l3 8H2z" fill="var(--icon-cyan)"/><circle cx="10" cy="13" r="2" fill="var(--footer-dark)"/></svg>
        <span>+000 12345 6789</span>
      </div>
      <div class="contact contact--email">
        <svg viewBox="0 0 20 20" aria-hidden="true"><circle cx="10" cy="10" r="8" fill="none" stroke="var(--icon-cyan)" stroke-width="1.8"/><path d="M3 8c4 2 10 2 14-2M4 14c4-3 9-4 14-2M9 2c-3 5-3 11 2 16" fill="none" stroke="var(--icon-cyan)" stroke-width="1.5"/></svg>
        <span>urname@email.com</span>
      </div>
    </div>
    <div class="color-band"><span></span><span></span><span></span><span></span><span></span></div>
  </footer>
</section>

<section class="page page--terms">
  <div class="brand"><span class="brand-mark"></span>FIRMLINE PAVING</div>
  <div class="header-rule"><span class="accent"></span><span class="base"></span></div>

  <div class="terms">
    <h2 class="terms-title">Terms and Conditions</h2>
    <ul class="terms-list">
      <li>Prices as quoted in this estimate are valid for (60) days only.</li>
      <li>Payment in full, less any previously paid amounts, is due to the Contractor upon completion of the proposed scope of work.</li>
      <li>All change order requests must be communicated in writing to the Contractor by the Client or their authorized representative.</li>
      <li>All measurements listed in this estimate are approximate and may vary slightly due to actual field conditions.</li>
      <li>It is agreed by the Contractor and the Client that complications and costs arising from unforeseen conditions and handling of unsuitable materials are not included in this estimate.</li>
      <li>Unless specifically listed in this estimate, the following items and their costs are not included: Maintenance of Traffic, Concrete Material Pumping, Testing, Excavation, Grading and Fill Material, Permits and Fees, Surveying and As-builts, Irrigation Repair, Landscaping and Root Mitigation, De-watering, Private Locates and Accessibility.</li>
      <li>Private utility locating services using radio detection devices and, when necessary, ground penetrating radar are offered by Firmline Paving to assist in finding private utilities that may not have been located by the public one call system. Firmline Paving will not be responsible for private utilities that have not been located nor for the failure of the above equipment to accurately detect existing utilities since the equipment is fallible and existing site conditions may preclude the ability of the equipment to detect an identifiable signal.</li>
    </ul>
  </div>

  <div class="sign-line" style="top:379px;width:88px"></div>
  <p class="sign-label" style="top:382px">Client Signature</p>
  <div class="sign-line" style="top:407px;width:83px"></div>
  <p class="sign-label" style="top:410px">Date</p>

  <footer class="footer">
    <div class="footer-bar">
      <div class="contact contact--phone">
        <svg viewBox="0 0 20 18" aria-hidden="true"><path d="M2 6c0-3 16-3 16 0v2h-4V6H6v2H2z M5 9h10l3 8H2z" fill="var(--icon-cyan)"/><circle cx="10" cy="13" r="2" fill="var(--footer-dark)"/></svg>
        <span>+000 12345 6789</span>
      </div>
      <div class="contact contact--email">
        <svg viewBox="0 0 20 20" aria-hidden="true"><circle cx="10" cy="10" r="8" fill="none" stroke="var(--icon-cyan)" stroke-width="1.8"/><path d="M3 8c4 2 10 2 14-2M4 14c4-3 9-4 14-2M9 2c-3 5-3 11 2 16" fill="none" stroke="var(--icon-cyan)" stroke-width="1.5"/></svg>
        <span>urname@email.com</span>
      </div>
    </div>
    <div class="color-band"><span></span><span></span><span></span><span></span><span></span></div>
  </footer>
</section>

</body>
</html>
```